Smartphone Social app needs an app design team

We need a smartphone app design for new company based in the NYC area called "qLoom Ventures, Inc." We are a smartphone application development company focused on utilizing uTether technologies to facilitate meeting and socializing with people that are in proximity to you.
Our first app is called qLoomtalk.net which helps people that are in physical proximity break the ice and encourages mingling with people at a party or an event.
The final design should communicate a sense of bringing social networking back to being human and meeting people in the real world.
Should be fun, contemporary, and communicate a sense of local area networking (physical world).
The scope of this design mockups that we are looking for would to design a people bingo like game for the phone facilitating meeting and breaking the ice with people in proximity with you.
When you’re ready to play, the game would provide each participant in proximity a bingo card with peoples profile characteristics and traits printed in each box. The guests have 30 minutes to mingle, introducing themselves, and find people who match the traits on the card. They must put the person’s profile picture in the corresponding box.
The first person to fill five boxes across or down yells BINGO! and that person wins the game.
Updates

Please see updated brief, describing more clearly the people bingo game concept. Thanks for your interest in designing this feature for our social app.

Reason: Changed and added more clarity to brief

Hi designers, I Updated the project brief to clarify Bingo game concept. Please add designs to simulate a bingo game concept. I know the size of the screen doesn't facilitate a bingo game, but think of way to get the same user experience with a small screen. Thanks, Dale

To all Designers, I have uploaded the new Logo for qLoomtalk and would like everyone to use the attached logos and assimilate the colors in the design. Thanks very much, Dale K.

Reason: Further clarification on app posted a few days ago.

Target Market(s)

Young adults 21-30
- College Students
- Young business professional

Industry/Entity Type

It Company

Font styles to use
Sans Serif

Requirements
Must have
• Ability to host an event
Message people in proximity to you to join the fun and download app
Build profile from GV and Trelmo
See profile and compatible traits and or dislikes (like went to same school, etc.)
Develop UX for a people bingo like game to get people to mingle and learn about each other

```html
<!DOCTYPE html>
<html lang="en">
<head>
<meta charset="utf-8">
<title>Time to mingle</title>
<link rel="stylesheet" href="https://fonts.googleapis.com/css2?family=Open+Sans:wght@300;400;600&display=swap">
<style>
  :root {
    --coral: #f26d6e;
    --coral-light: #f68b8b;
    --white: #ffffff;
    --page: #ffffff;
    --ink-soft: #b9b9b9;
    --trait: #a9a9a9;
    --trait-faded: #c9c9c9;
    --rule: #dedede;
    --ring-track: #eeeee9;
    --ring-red: #f1665c;
    --ring-yellow: #f6d55e;
    --tick: #76bf62;
  }
  * { box-sizing: border-box; margin: 0; padding: 0; }
  html, body { width: 1200px; height: 2166px; overflow: hidden; background: var(--page); }
  body { font-family: "Open Sans", Arial, sans-serif; position: relative; }

  .app-bar {
    position: absolute; left: 0; top: 0; width: 1200px; height: 226px;
    background: linear-gradient(90deg, var(--coral) 0%, var(--coral) 55%, var(--coral-light) 100%);
    color: var(--white);
  }
  .status-bar {
    position: absolute; left: 0; top: 0; width: 100%; height: 86px;
    font-weight: 600; font-size: 42px;
  }
  .status-left { position: absolute; left: 30px; top: 18px; display: flex; align-items: center; gap: 14px; }
  .status-time { position: absolute; left: 0; right: 0; top: 18px; text-align: center; }
  .status-right { position: absolute; right: 24px; top: 18px; display: flex; align-items: center; gap: 16px; }

  .nav { position: absolute; left: 0; top: 86px; width: 100%; height: 140px; }
  .nav-title {
    position: absolute; left: 0; right: 0; top: 38px; text-align: center;
    font-weight: 300; font-size: 56px; letter-spacing: 0.5px;
  }
  .nav-menu { position: absolute; left: 70px; top: 48px; }
  .nav-profile { position: absolute; right: 56px; top: 40px; }

  .timer {
    position: absolute; left: 400px; top: 310px; width: 400px; height: 400px;
  }
  .timer svg { position: absolute; inset: 0; }
  .timer-face {
    position: absolute; left: 52px; top: 52px; width: 296px; height: 296px; border-radius: 50%;
    background: #f9f9f9; box-shadow: 0 4px 14px rgba(0,0,0,0.08);
    display: flex; flex-direction: column; align-items: center; justify-content: center;
    color: var(--ink-soft);
  }
  .timer-count { font-weight: 300; font-size: 78px; line-height: 1; }
  .timer-label { font-weight: 300; font-size: 42px; margin-top: 6px; }

  .bingo-card {
    position: absolute; left: 24px; top: 818px; width: 1154px; height: 1290px;
    border: 2px solid var(--rule); border-radius: 22px; overflow: hidden;
    display: grid; grid-template-columns: repeat(5, 1fr); grid-template-rows: repeat(5, 1fr);
    background: var(--white);
  }
  .cell { position: relative; border-right: 2px solid var(--rule); border-bottom: 2px solid var(--rule); }
  .cell:nth-child(5n) { border-right: none; }
  .cell:nth-child(n+21) { border-bottom: none; }

  .trait-list {
    display: flex; flex-direction: column; align-items: center; justify-content: center;
    font-weight: 400; font-size: 27px; line-height: 49px; color: var(--trait);
  }
  .trait-list.is-faded { color: var(--trait-faded); }

  .profile-photo { padding: 10px; }
  .photo-fill { width: 100%; height: 100%; }
  .tone-warm { background: linear-gradient(160deg, #7a4a3a, #d79b84 55%, #3b2a26); }
  .tone-pink { background: linear-gradient(160deg, #c86c7c, #e6b3a8 55%, #6e2a3e); }
  .tone-light { background: linear-gradient(160deg, #e9dbc9, #caa480 55%, #8a6a52); }
  .tone-dark { background: linear-gradient(160deg, #2f3d52, #b98570 55%, #1e2a33); }
  .tone-teal { background: linear-gradient(160deg, #3d6d6a, #c49a72 55%, #2a2420); }
  .tone-grey { background: linear-gradient(160deg, #b8b4b0, #d8c0b0 55%, #6a5c56); }

  .match-tick { position: absolute; right: 12px; top: 16px; width: 48px; height: 48px; }
</style>
</head>
<body>
  <header class="app-bar">
    <div class="status-bar">
      <div class="status-left">
        <svg width="124" height="26" viewBox="0 0 124 26" aria-hidden="true">
          <circle cx="13" cy="13" r="10" fill="#fff"/>
          <circle cx="37" cy="13" r="10" fill="#fff"/>
          <circle cx="61" cy="13" r="10" fill="#fff"/>
          <circle cx="85" cy="13" r="9" fill="none" stroke="#fff" stroke-width="2.5"/>
          <circle cx="109" cy="13" r="9" fill="none" stroke="#fff" stroke-width="2.5"/>
        </svg>
        <span>BELL</span>
        <svg width="46" height="34" viewBox="0 0 46 34" aria-hidden="true">
          <path d="M3 12 A28 28 0 0 1 43 12" fill="none" stroke="#fff" stroke-width="5" stroke-linecap="round"/>
          <path d="M10 19 A18 18 0 0 1 36 19" fill="none" stroke="#fff" stroke-width="5" stroke-linecap="round"/>
          <path d="M23 32 L16 25 A10 10 0 0 1 30 25 Z" fill="#fff"/>
        </svg>
      </div>
      <div class="status-time">4:21 PM</div>
      <div class="status-right">
        <svg width="24" height="40" viewBox="0 0 24 40" aria-hidden="true">
          <path d="M4 11 L19 27 L11 35 V5 L19 13 L4 29" fill="none" stroke="rgba(255,255,255,0.75)" stroke-width="3" stroke-linejoin="round"/>
        </svg>
        <span>100%</span>
        <svg width="92" height="40" viewBox="0 0 92 40" aria-hidden="true">
          <rect x="2" y="6" width="80" height="28" rx="4" fill="none" stroke="#fff" stroke-width="3"/>
          <rect x="7" y="11" width="70" height="18" rx="2" fill="#fff"/>
          <rect x="84" y="14" width="5" height="12" rx="2" fill="#fff"/>
        </svg>
      </div>
    </div>
    <nav class="nav">
      <svg class="nav-menu" width="50" height="44" viewBox="0 0 50 44" aria-label="Menu" role="img">
        <rect x="0" y="2" width="8" height="6" fill="#fff"/><rect x="13" y="2" width="37" height="6" fill="#fff"/>
        <rect x="0" y="14" width="8" height="6" fill="#fff"/><rect x="13" y="14" width="37" height="6" fill="#fff"/>
        <rect x="0" y="26" width="8" height="6" fill="#fff"/><rect x="13" y="26" width="37" height="6" fill="#fff"/>
        <rect x="0" y="38" width="8" height="6" fill="#fff"/><rect x="13" y="38" width="37" height="6" fill="#fff"/>
      </svg>
      <h1 class="nav-title">Time to mingle</h1>
      <svg class="nav-profile" width="54" height="54" viewBox="0 0 54 54" aria-label="Profile" role="img">
        <ellipse cx="27" cy="16" rx="12" ry="14" fill="#fff"/>
        <path d="M2 54 C2 38 14 33 27 33 C40 33 52 38 52 54 Z" fill="#fff"/>
      </svg>
    </nav>
  </header>

  <section class="timer" aria-label="Game timer">
    <svg width="400" height="400" viewBox="0 0 400 400" aria-hidden="true">
      <defs>
        <linearGradient id="ringGradient" x1="0" y1="0" x2="0" y2="1">
          <stop offset="0" stop-color="var(--ring-red)"/>
          <stop offset="1" stop-color="var(--ring-yellow)"/>
        </linearGradient>
      </defs>
      <circle cx="200" cy="200" r="196" fill="#fdfdfb"/>
      <circle cx="200" cy="200" r="188" fill="none" stroke="var(--ring-track)" stroke-width="8"/>
      <circle cx="200" cy="200" r="188" fill="none" stroke="url(#ringGradient)" stroke-width="9"
              stroke-dasharray="710 1200" transform="rotate(-90 200 200)"/>
    </svg>
    <div class="timer-face">
      <div class="timer-count">28:52</div>
      <div class="timer-label">time left</div>
    </div>
  </section>

  <main class="bingo-card" aria-label="Bingo card">
    <!-- row 1 -->
    <div class="cell trait-list"><span>Tall</span><span>Sweet</span><span>Wear a cap</span><span>Cali College</span></div>
    <div class="cell profile-photo"><div class="photo-fill tone-dark" role="img" aria-label="Profile photo of a guest in sunglasses"></div></div>
    <div class="cell trait-list"><span>Tall</span><span>Sweet</span><span>Wear a cap</span><span>Cali College</span></div>
    <div class="cell profile-photo"><div class="photo-fill tone-grey" role="img" aria-label="Profile photo of a guest with short hair"></div></div>
    <div class="cell profile-photo"><div class="photo-fill tone-pink" role="img" aria-label="Profile photo of a guest with long hair"></div></div>
    <!-- row 2 -->
    <div class="cell profile-photo"><div class="photo-fill tone-light" role="img" aria-label="Profile photo of a guest wearing a cap"></div>
      <svg class="match-tick" viewBox="0 0 48 48" aria-hidden="true"><circle cx="24" cy="24" r="23" fill="var(--tick)"/><path d="M13 24 L21 32 L35 17" fill="none" stroke="#fff" stroke-width="4.5" stroke-linecap="round" stroke-linejoin="round"/></svg></div>
    <div class="cell trait-list"><span>Tall</span><span>Sweet</span><span>Wear a cap</span><span>Cali College</span></div>
    <div class="cell profile-photo"><div class="photo-fill tone-pink" role="img" aria-label="Profile photo of a guest wearing a bandana"></div>
      <svg class="match-tick" viewBox="0 0 48 48" aria-hidden="true"><circle cx="24" cy="24" r="23" fill="var(--tick)"/><path d="M13 24 L21 32 L35 17" fill="none" stroke="#fff" stroke-width="4.5" stroke-linecap="round" stroke-linejoin="round"/></svg></div>
    <div class="cell profile-photo"><div class="photo-fill tone-light" role="img" aria-label="Profile photo of a smiling blonde guest"></div></div>
    <div class="cell trait-list is-faded"><span>Tall</span><span>Sweet</span><span>Wear a cap</span><span>Cali College</span></div>
    <!-- row 3 -->
    <div class="cell profile-photo"><div class="photo-fill tone-teal" role="img" aria-label="Profile photo of a guest with wavy hair"></div>
      <svg class="match-tick" viewBox="0 0 48 48" aria-hidden="true"><circle cx="24" cy="24" r="23" fill="var(--tick)"/><path d="M13 24 L21 32 L35 17" fill="none" stroke="#fff" stroke-width="4.5" stroke-linecap="round" stroke-linejoin="round"/></svg></div>
    <div class="cell profile-photo"><div class="photo-fill tone-pink" role="img" aria-label="Profile photo of a guest with long hair"></div></div>
    <div class="cell trait-list"><span>Tall</span><span>Sweet</span><span>Wear a cap</span><span>Cali College</span></div>
    <div class="cell profile-photo"><div class="photo-fill tone-dark" role="img" aria-label="Profile photo of a guest in sunglasses"></div></div>
    <div class="cell trait-list"><span>Tall</span><span>Sweet</span><span>Wear a cap</span><span>Cali College</span></div>
    <!-- row 4 -->
    <div class="cell profile-photo"><div class="photo-fill tone-light" role="img" aria-label="Profile photo of a smiling guest"></div></div>
    <div class="cell profile-photo"><div class="photo-fill tone-warm" role="img" aria-label="Profile photo of a guest with a fringe"></div></div>
    <div class="cell profile-photo"><div class="photo-fill tone-grey" role="img" aria-label="Profile photo of a guest in red sunglasses"></div></div>
    <div class="cell profile-photo"><div class="photo-fill tone-grey" role="img" aria-label="Profile photo of a guest with short hair"></div>
      <svg class="match-tick" viewBox="0 0 48 48" aria-hidden="true"><circle cx="24" cy="24" r="23" fill="var(--tick)"/><path d="M13 24 L21 32 L35 17" fill="none" stroke="#fff" stroke-width="4.5" stroke-linecap="round" stroke-linejoin="round"/></svg></div>
    <div class="cell profile-photo"><div class="photo-fill tone-light" role="img" aria-label="Profile photo of a guest wearing a cap"></div></div>
    <!-- row 5 -->
    <div class="cell trait-list"><span>Tall</span><span>Sweet</span><span>Wear a cap</span><span>Cali College</span></div>
    <div class="cell profile-photo"><div class="photo-fill tone-pink" role="img" aria-label="Profile photo of a guest wearing a bandana"></div>
      <svg class="match-tick" viewBox="0 0 48 48" aria-hidden="true"><circle cx="24" cy="24" r="23" fill="var(--tick)"/><path d="M13 24 L21 32 L35 17" fill="none" stroke="#fff" stroke-width="4.5" stroke-linecap="round" stroke-linejoin="round"/></svg></div>
    <div class="cell profile-photo"><div class="photo-fill tone-teal" role="img" aria-label="Profile photo of a guest with wavy hair"></div>
      <svg class="match-tick" viewBox="0 0 48 48" aria-hidden="true"><circle cx="24" cy="24" r="23" fill="var(--tick)"/><path d="M13 24 L21 32 L35 17" fill="none" stroke="#fff" stroke-width="4.5" stroke-linecap="round" stroke-linejoin="round"/></svg></div>
    <div class="cell trait-list"><span>Tall</span><span>Sweet</span><span>Wear a cap</span><span>Cali College</span></div>
    <div class="cell profile-photo"><div class="photo-fill tone-teal" role="img" aria-label="Profile photo of a guest with wavy hair"></div></div>
  </main>
</body>
</html>
```